Boring Fiberglass Repair Company needs creative business cards

The Fiberglass Repair industry isn't very fun or creative but we'd like a business card that communicates a fresh, modern, and service-oriented feel. We repair bathroom fixtures (bath tubs, showers, etc) which are made out of fiberglass. Our fiberglass repair service will be sold to bathtub manufacturers and also businesses that sell bathtubs. We will also offer our services to home owners that have broken showers and bathtubs.
Target Market(s)
Home builders, plumbing wholesalers, home owners
Contact Information for Business Card
Name
Phone Number
Email Address
Business Address
Tag line: "Quality Craftsmanship Today"
Look and feel

```html
<!DOCTYPE html>
<html lang="en">
<head>
<meta charset="utf-8">
<title>Mesa Ridge Fiberglass — Business Card</title>
<link rel="stylesheet" href="https://fonts.googleapis.com/css2?family=Poppins:wght@400;500;700;800&display=swap">
<style>
  :root {
    --navy: #0d2350;
    --orange: #f18a21;
    --white: #ffffff;
    --ink: #1a1a1a;
    --stage: #2a2a2c;
  }
  * { margin: 0; padding: 0; box-sizing: border-box; }
  html, body { width: 1200px; height: 900px; overflow: hidden; }
  body {
    background: var(--stage);
    font-family: "Poppins", sans-serif;
    position: relative;
  }
  .card {
    position: absolute;
    width: 600px;
    height: 343px;
    border-radius: 22px;
    overflow: hidden;
  }
  .card--front {
    left: 300px; top: 62px;
    background: var(--navy);
    color: var(--white);
  }
  .card--back {
    left: 300px; top: 495px;
    background: var(--white);
  }
  .brand-name {
    font-weight: 800;
    text-transform: uppercase;
    line-height: 1.05;
    letter-spacing: 1px;
  }
  .card--front .brand-name {
    position: absolute;
    left: 0; right: 0; top: 100px;
    text-align: center;
    font-size: 40px;
    color: var(--white);
  }
  .brand-name .brand-sub {
    display: block;
    font-size: 20px;
    letter-spacing: 12px;
    margin-top: 6px;
  }
  .tagline {
    position: absolute;
    left: 0; right: 0; bottom: 50px;
    text-align: center;
    font-size: 17px;
    font-weight: 500;
    letter-spacing: 0.5px;
  }
  .card--back .brand-name {
    position: absolute;
    left: 40px; top: 120px;
    width: 250px;
    font-size: 31px;
    color: var(--navy);
  }
  .card--back .brand-name .brand-sub {
    font-size: 16px;
    letter-spacing: 9px;
  }
  .divider {
    position: absolute;
    left: 300px; top: 40px;
    width: 2px; height: 205px;
    background: var(--navy);
  }
  .contact {
    position: absolute;
    left: 320px; top: 34px;
    width: 270px;
  }
  .person-name {
    font-weight: 800;
    font-size: 23px;
    color: var(--navy);
    line-height: 1.05;
  }
  .person-role {
    font-weight: 700;
    font-size: 13px;
    color: var(--orange);
    letter-spacing: 0.5px;
    margin-bottom: 12px;
  }
  .contact-list { list-style: none; }
  .contact-item {
    display: flex;
    align-items: flex-start;
    gap: 9px;
    font-size: 12.5px;
    color: var(--ink);
    line-height: 1.4;
    margin-bottom: 6px;
  }
  .contact-icon { width: 14px; height: 14px; flex: none; margin-top: 2px; }
  .card-bands { position: absolute; left: 0; bottom: 0; width: 600px; height: 50px; }
</style>
</head>
<body>

<section class="card card--front" aria-label="Card front">
  <h1 class="brand-name">Mesa Ridge<span class="brand-sub">Fiberglass</span></h1>
  <p class="tagline">Quality Craftsmanship Today</p>
</section>

<section class="card card--back" aria-label="Card back">
  <h2 class="brand-name">Mesa Ridge<span class="brand-sub">Fiberglass</span></h2>
  <div class="divider"></div>
  <div class="contact">
    <p class="person-name">DANIEL REYES</p>
    <p class="person-role">CEO/FOUNDER</p>
    <ul class="contact-list">
      <li class="contact-item">
        <svg class="contact-icon" viewBox="0 0 24 24"><path fill="#f18a21" d="M6.6 10.8a15 15 0 0 0 6.6 6.6l2.2-2.2c.3-.3.7-.4 1-.2 1.1.4 2.3.6 3.6.6.6 0 1 .4 1 1V20c0 .6-.4 1-1 1A17 17 0 0 1 3 4c0-.6.4-1 1-1h3.5c.6 0 1 .4 1 1 0 1.3.2 2.5.6 3.6.1.3 0 .7-.2 1z"/></svg>
        <span>555-013-4821</span>
      </li>
      <li class="contact-item">
        <svg class="contact-icon" viewBox="0 0 24 24"><rect x="2" y="5" width="20" height="14" rx="1" fill="#f18a21"/><path d="M3 6l9 7 9-7" fill="none" stroke="#fff" stroke-width="1.6"/></svg>
        <span>daniel@mesaridgemail.com</span>
      </li>
      <li class="contact-item">
        <svg class="contact-icon" viewBox="0 0 24 24"><g fill="none" stroke="#f18a21" stroke-width="1.8"><circle cx="12" cy="12" r="9.5"/><ellipse cx="12" cy="12" rx="4" ry="9.5"/><path d="M2.5 12h19M4 7h16M4 17h16"/></g></svg>
        <span>www.mesaridgerepair.com</span>
      </li>
      <li class="contact-item">
        <svg class="contact-icon" viewBox="0 0 24 24"><path fill="#f18a21" d="M12 2a7 7 0 0 0-7 7c0 5 7 13 7 13s7-8 7-13a7 7 0 0 0-7-7zm0 9.5A2.5 2.5 0 1 1 12 6.5a2.5 2.5 0 0 1 0 5z"/></svg>
        <span>418 Alder Street NW<br>Suite 210, Lakeview<br>MI 49850</span>
      </li>
    </ul>
  </div>
  <svg class="card-bands" viewBox="0 0 600 50" preserveAspectRatio="none" aria-hidden="true">
    <polygon points="0,28 350,28 372,50 0,50" fill="#0d2350"/>
    <polygon points="354,28 600,0 600,14 376,50 372,50" fill="#f18a21"/>
    <polygon points="376,50 600,14 600,50" fill="#0d2350"/>
  </svg>
</section>

</body>
</html>
```